Beekeeper needs box/label design for honey/CBD and other honey-related products

We need a box (or label) design for a beekeeping company in Virginia called Tamsin Hollow Farm. Our products will include honey mixed with CBD oil and other essential oils (vanilla, lavender, etc).The box design should be scalable to include several different honey/oil products. We would like to incorporate our current farm logo into the design. Here is a link to a honey producing company with a series of products using their honey mixed with certain oils. It's a good reference of what type box/label design we would like (https://corbinandlyle.co/pages/honey).

Target Market(s)

Retail stores and consumers

Requirements
Must have
• Tamsin Hollow Farm name and logo

```html
<!DOCTYPE html>
<html lang="en">
<head>
<meta charset="utf-8">
<title>Tamsin Hollow Farm – Raw Honey with CBD Oil</title>
<link rel="stylesheet" href="https://fonts.googleapis.com/css2?family=Cinzel:wght@400&family=Montserrat:wght@500;600&family=Roboto+Condensed:wght@700&display=swap">
<style>
  :root {
    --bg: #ebebe8;
    --green-light: #c4cf6a;
    --green-mid: #a4b640;
    --green-deep: #8a9c2e;
    --olive-band: #505a1c;
    --olive-ink: #4e5419;
    --cream: #f1f1ea;
    --gold: #e0a91a;
    --leaf: #6f9a24;
  }
  * { margin: 0; padding: 0; box-sizing: border-box; }
  html, body { width: 1200px; height: 878px; overflow: hidden; background: var(--bg); }
  .canvas { position: relative; width: 1200px; height: 878px; }

  .panel {
    position: absolute;
    overflow: hidden;
    display: flex;
    flex-direction: column;
  }
  .panel__pattern {
    position: absolute; inset: 0;
    background:
      radial-gradient(ellipse at 30% 10%, rgba(255,255,255,0.35), transparent 55%),
      linear-gradient(160deg, var(--green-light) 0%, var(--green-mid) 60%, var(--green-deep) 100%);
  }
  .panel__body {
    position: relative;
    flex: 1;
    display: flex; flex-direction: column; align-items: center;
  }
  .panel__band {
    position: relative;
    background: var(--olive-band);
    display: flex; align-items: center; justify-content: center; gap: 14px;
  }

  .logo-square { border: 6px solid var(--olive-ink); background: var(--cream); }
  .brand-name {
    font-family: "Cinzel", serif; font-weight: 400; color: var(--olive-ink);
    text-align: center; line-height: 1;
  }
  .brand-name__sub { display: block; letter-spacing: 0.35em; margin-top: 10px; }
  .rule { height: 3px; background: var(--olive-ink); }
  .product-name {
    font-family: "Montserrat", sans-serif; font-weight: 600; color: var(--olive-ink);
    letter-spacing: 0.01em;
  }
  .oil-mark { display: block; }
  .oil-claim { font-family: "Montserrat", sans-serif; font-weight: 500; color: var(--cream); line-height: 1.05; }
  .oil-claim__small { display: block; }
  .oil-claim__large { display: block; font-weight: 600; }

  /* jar label */
  .jar-label { left: 40px; top: 230px; width: 500px; height: 430px; }
  .jar-label .panel__body { padding-top: 28px; }
  .jar-label .logo-square { width: 150px; height: 150px; }
  .jar-label .brand-name { font-size: 50px; margin-top: 18px; }
  .jar-label .brand-name__sub { font-size: 17px; }
  .jar-label .rule { width: 300px; margin-top: 16px; }
  .jar-label .product-name { font-size: 28px; margin-top: 16px; }
  .jar-label .panel__band { height: 96px; }
  .jar-label .oil-claim__small { font-size: 20px; }
  .jar-label .oil-claim__large { font-size: 32px; }

  /* box side */
  .box-side { left: 590px; top: 40px; width: 190px; height: 800px; }
  .box-side .panel__body { padding: 380px 18px 0; align-items: flex-start; }
  .box-side .panel__band { height: 180px; }
  .side-copy {
    font-family: "Roboto Condensed", sans-serif; font-weight: 700;
    font-size: 11.5px; line-height: 1.5; color: #1e2208;
  }

  /* box front */
  .box-front { left: 780px; top: 40px; width: 390px; height: 800px; }
  .box-front .panel__body { padding-top: 150px; }
  .box-front .logo-square { width: 200px; height: 200px; }
  .box-front .brand-name { font-size: 62px; margin-top: 40px; }
  .box-front .brand-name__sub { font-size: 21px; margin-top: 18px; }
  .box-front .rule { width: 340px; margin-top: 24px; }
  .box-front .product-name { font-size: 36px; margin-top: 24px; }
  .box-front .panel__band { height: 180px; }
  .box-front .oil-claim__small { font-size: 26px; }
  .box-front .oil-claim__large { font-size: 42px; }
</style>
</head>
<body>
<main class="canvas">

  <section class="panel jar-label" aria-label="Jar label">
    <div class="panel__pattern" role="img" aria-label="Green honeycomb pattern background"></div>
    <div class="panel__body">
      <div class="logo-square" aria-hidden="true"></div>
      <h1 class="brand-name">Tamsin<span class="brand-name__sub">Hollow Farm</span></h1>
      <div class="rule"></div>
      <p class="product-name">RAW HONEY</p>
    </div>
    <div class="panel__band">
      <svg class="oil-mark" width="64" height="72" viewBox="0 0 64 72" role="img" aria-label="Oil drop over a hemp leaf">
        <ellipse cx="28" cy="56" rx="26" ry="12" fill="var(--leaf)"/>
        <path d="M38 4 C32 20 26 28 26 38 a12 12 0 0 0 24 0 C50 28 44 20 38 4Z" fill="var(--gold)"/>
      </svg>
      <p class="oil-claim"><span class="oil-claim__small">with</span><span class="oil-claim__large">CBD OIL</span></p>
    </div>
  </section>

  <section class="panel box-side" aria-label="Box side panel">
    <div class="panel__pattern" role="img" aria-label="Green honeycomb pattern background"></div>
    <div class="panel__body">
      <p class="side-copy">Raw honey gathered from our hives in the Virginia hills, gently blended with pure CBD oil. Unheated and unfiltered to keep its natural pollen and flavour. Stir into tea, drizzle over toast or take a spoonful each day. Store at room temperature and keep out of direct sunlight. Crystals are natural; warm gently to soften.</p>
    </div>
    <div class="panel__band"></div>
  </section>

  <section class="panel box-front" aria-label="Box front panel">
    <div class="panel__pattern" role="img" aria-label="Green honeycomb pattern background"></div>
    <div class="panel__body">
      <div class="logo-square" aria-hidden="true"></div>
      <h2 class="brand-name">Tamsin<span class="brand-name__sub">Hollow Farm</span></h2>
      <div class="rule"></div>
      <p class="product-name">RAW HONEY</p>
    </div>
    <div class="panel__band">
      <svg class="oil-mark" width="92" height="104" viewBox="0 0 64 72" role="img" aria-label="Oil drop over a hemp leaf">
        <ellipse cx="28" cy="56" rx="26" ry="12" fill="var(--leaf)"/>
        <path d="M38 4 C32 20 26 28 26 38 a12 12 0 0 0 24 0 C50 28 44 20 38 4Z" fill="var(--gold)"/>
      </svg>
      <p class="oil-claim"><span class="oil-claim__small">with</span><span class="oil-claim__large">CBD OIL</span></p>
    </div>
  </section>

</main>
</body>
</html>
```